Business card design to suit our website

Need a nice looking business card for our business based off images from our Website and provided images. The business card will require 2 different names (for the 2 owners). The business card should include images from our website, facebook (keel bracket works set) or the pictures provided. it should also contain all contact information.
Our website is www.keelbracketworks.com.au
Please dont use image from top bar of website. If images are used please use the ones of our product under the buy it now tab

Target Market(s)

Automotive

Industry/Entity Type

Automotive Part

Contact Information for Business Card

Business Name. contact details including names phone number email. logo
2 business cards needed with 2 different persons names and phone number.

Colors

Designer to choose colors to be used in the design.

Requirements
Must have
• whatever looks best

```html
<!DOCTYPE html>
<html lang="en">
<head>
<meta charset="utf-8">
<title>Keel Bracket Works Set – Business Cards</title>
<link href="https://fonts.googleapis.com/css2?family=Saira:wght@400;600;700&display=swap" rel="stylesheet">
<style>
  :root {
    --stage: #e7e4df;
    --red: #d81a24;
    --red-deep: #8e0c12;
    --red-bright: #f0323a;
    --black: #141414;
    --silver-light: #f4f5f6;
    --silver-mid: #d3d6da;
    --silver-dark: #a9adb2;
    --ink: #2a2a2a;
    --white: #ffffff;
  }
  * { box-sizing: border-box; margin: 0; padding: 0; }
  html, body { width: 1200px; height: 800px; overflow: hidden; }
  body {
    background: var(--stage);
    font-family: "Saira", "Arial", sans-serif;
    position: relative;
  }
  .card {
    position: absolute;
    width: 540px;
    height: 315px;
    top: 242px;
    overflow: hidden;
    border-radius: 4px;
    box-shadow: 0 6px 18px rgba(0,0,0,0.18);
  }
  .card--back { left: 40px; }
  .card--front { left: 620px; }
  .card__art { position: absolute; inset: 0; }

  .brand-name {
    position: absolute;
    font-weight: 700;
    color: var(--silver-light);
    line-height: 1;
    letter-spacing: 0.5px;
  }
  .card--front .brand-name { left: 34px; top: 30px; font-size: 34px; width: 330px; }
  .card--back .brand-name { left: 150px; top: 212px; font-size: 24px; width: 260px; }

  .holder { position: absolute; left: 34px; top: 150px; color: var(--white); }
  .holder__name { font-size: 21px; font-weight: 400; line-height: 1.1; }
  .holder__role { font-size: 11px; color: #f6d3d4; }

  .contacts { position: absolute; left: 34px; top: 206px; list-style: none; }
  .contacts li {
    display: flex; align-items: center; gap: 10px;
    color: var(--white); font-size: 17px; line-height: 28px;
  }
  .contacts svg { width: 16px; height: 16px; flex: none; }

  .tagline {
    position: absolute; left: 52px; top: 82px; width: 360px;
    font-size: 15px; line-height: 1.45; letter-spacing: 1.6px;
    color: var(--ink); font-weight: 600; text-align: center;
  }
  .follow {
    position: absolute; left: 34px; top: 280px;
    display: flex; align-items: center; gap: 8px;
    color: var(--black); font-size: 15px;
  }
  .follow__dot { width: 16px; height: 16px; border-radius: 50%; background: var(--black); }
</style>
</head>
<body>

  <!-- Back of card -->
  <section class="card card--back">
    <svg class="card__art" viewBox="0 0 540 315" width="540" height="315">
      <defs>
        <linearGradient id="backSilver" x1="0" y1="0" x2="1" y2="1">
          <stop offset="0" stop-color="#f6f7f8"/>
          <stop offset="1" stop-color="#cfd2d6"/>
        </linearGradient>
        <linearGradient id="backRed" x1="0" y1="0" x2="1" y2="1">
          <stop offset="0" stop-color="#a5101a"/>
          <stop offset="0.5" stop-color="#e0222b"/>
          <stop offset="1" stop-color="#8e0c12"/>
        </linearGradient>
        <radialGradient id="partsTone" cx="0.5" cy="0.5" r="0.6">
          <stop offset="0" stop-color="#eef0f2"/>
          <stop offset="1" stop-color="#b6bbc1"/>
        </radialGradient>
      </defs>
      <rect width="540" height="315" fill="url(#backSilver)"/>
      <rect x="80" y="14" width="230" height="200" rx="20" fill="url(#partsTone)" opacity="0.8"
            role="img" aria-label="Photo of aluminium switch housings and kit parts"/>
      <path d="M0,205 C140,215 300,215 420,175 C470,158 510,128 540,95 V315 H0 Z" fill="url(#backRed)"/>
      <path d="M395,182 C460,158 505,125 540,85 V100 C505,138 462,168 405,186 Z" fill="var(--black)"/>
      <path d="M0,262 H540 V315 H0 Z" fill="#a0a3a6" opacity="0.35"/>
      <rect x="420" y="92" width="110" height="60" rx="18" fill="var(--red-bright)"
            role="img" aria-label="Photo of a red sports car"/>
    </svg>
    <p class="tagline">Remove, Rebuild, Replace your ignition switch without removing the steering column with a high quality aluminium switch housing. With a lifetime warranty.</p>
    <div class="brand-name">Keel Bracket Works Set</div>
    <div class="follow"><span>Follow us on</span><span class="follow__dot"></span></div>
  </section>

  <!-- Front of card -->
  <section class="card card--front">
    <svg class="card__art" viewBox="0 0 540 315" width="540" height="315">
      <defs>
        <linearGradient id="frontSilver" x1="0" y1="0" x2="1" y2="1">
          <stop offset="0" stop-color="#f7f8f9"/>
          <stop offset="1" stop-color="#c6cacf"/>
        </linearGradient>
        <linearGradient id="frontRed" x1="0" y1="0" x2="1" y2="1">
          <stop offset="0" stop-color="#9a0e16"/>
          <stop offset="0.45" stop-color="#e4242d"/>
          <stop offset="1" stop-color="#a3101a"/>
        </linearGradient>
        <radialGradient id="kitTone" cx="0.5" cy="0.5" r="0.6">
          <stop offset="0" stop-color="#e9ebee"/>
          <stop offset="1" stop-color="#8b9097"/>
        </radialGradient>
      </defs>
      <rect width="540" height="315" fill="url(#frontSilver)"/>
      <path d="M0,0 H540 V40 C470,55 420,85 395,130 C370,180 365,250 400,315 H0 Z" fill="url(#frontRed)"/>
      <path d="M540,40 C470,55 420,85 395,130 C370,180 365,250 400,315 H388 C350,250 355,175 382,126 C410,78 460,48 540,32 Z" fill="var(--black)"/>
      <rect x="405" y="92" width="125" height="200" rx="18" fill="url(#kitTone)"
            role="img" aria-label="Photo of the bracket kit: housing, key barrel and mounting bolts"/>
    </svg>
    <div class="brand-name">Keel Bracket Works Set</div>
    <div class="holder">
      <p class="holder__name">Dale Harker</p>
      <p class="holder__role">Owner</p>
    </div>
    <ul class="contacts">
      <li>
        <svg viewBox="0 0 16 16"><circle cx="8" cy="8" r="8" fill="#c9ccd0"/><path d="M5.5 4h1.6l.7 2-1 .8a5 5 0 0 0 2.4 2.4l.8-1 2 .7v1.6c0 .5-.4.9-.9.9A7 7 0 0 1 4.6 4.9c0-.5.4-.9.9-.9z" fill="#555"/></svg>
        <span>1300 555 017</span>
      </li>
      <li>
        <svg viewBox="0 0 16 16"><circle cx="8" cy="8" r="8" fill="#c9ccd0"/><rect x="4" y="5" width="8" height="6" rx="1" fill="none" stroke="#555" stroke-width="1.2"/><path d="M4.3 5.4 8 8.3l3.7-2.9" fill="none" stroke="#555" stroke-width="1.2"/></svg>
        <span>sales@keelbracketworks.com.au</span>
      </li>
      <li>
        <svg viewBox="0 0 16 16"><circle cx="8" cy="8" r="8" fill="#c9ccd0"/><circle cx="8" cy="8" r="4" fill="none" stroke="#555" stroke-width="1.1"/><path d="M4 8h8M8 4c-1.6 2.2-1.6 5.8 0 8M8 4c1.6 2.2 1.6 5.8 0 8" fill="none" stroke="#555" stroke-width="1"/></svg>
        <span>www.keelbracketworks.com.au</span>
      </li>
    </ul>
  </section>

</body>
</html>
```